Lift Her Forward, 2019 Save The Date

Please develop a save the date flyer our 4th Annual Lift Her Forward and See Her Rise! This event is focused on maintaining participation and appreciation for women in the design and construction industry.

This unique Forum provides a venue to engage everyone from executives to those just beginning their careers with active, hands-on sessions and vibrant networking with the best and brightest in the A/E/C industry. In our usual Q-TarVM Forum style, Keynotes become table participants and table participants become presenters, encouraging participants to assimilate what they are learning. Join local, state and national leaders and subject matter experts as we candidly explore and address the issues affecting women in our industry.

Industry/Entity Type

Construction

Font styles to use
Sans Serif

Requirements
Must have
• This is a save the date, Must have:
• Q-TarVM Logo
• Title: 4th Annual Lift Her Forward and See Her Rise!
• Date: January 25, 2019
• Location: Harbor Crest Resort and Spa, San Marcos, TX
Nice to have
• A header that can easily be pulled to add to other marketing materials and for use across other platforms (web, etc.).

```html
<!DOCTYPE html>
<html lang="en">
<head>
<meta charset="utf-8">
<title>Lift Her Forward – Save The Date</title>
<link rel="stylesheet" href="https://fonts.googleapis.com/css2?family=Bebas+Neue&family=Oswald:wght@400;500&family=Montserrat:wght@500&family=Open+Sans:wght@400&display=swap">
<style>
  :root {
    --page-bg: #ffffff;
    --brand-blue: #2b4ea3;
    --brand-blue-deep: #1f3a8a;
    --title-blue: #24469c;
    --accent-green: #8cb63c;
    --band-gray: #5a5a5c;
    --text-gray: #444446;
    --box-border: #a9a9ab;
    --white: #ffffff;
  }
  html, body {
    margin: 0;
    padding: 0;
    width: 1200px;
    height: 1200px;
    overflow: hidden;
    background: var(--page-bg);
  }
  .flyer {
    position: absolute;
    left: 259px;
    top: 118px;
    width: 682px;
    height: 962px;
    background: var(--white);
    box-shadow: 0 4px 14px rgba(0,0,0,0.18);
    overflow: hidden;
  }
  .flyer-art {
    position: absolute;
    inset: 0;
  }
  .brand {
    position: absolute;
    left: 163px;
    top: 48px;
    display: flex;
    align-items: center;
    gap: 28px;
  }
  .brand-mark {
    width: 108px;
    height: 108px;
    border-radius: 50%;
    background: var(--white);
  }
  .brand-text {
    color: var(--white);
  }
  .brand-name {
    font-family: "Montserrat", sans-serif;
    font-weight: 500;
    font-size: 52px;
    line-height: 1;
    letter-spacing: 1px;
    padding-bottom: 8px;
    border-bottom: 1.5px solid rgba(255,255,255,0.85);
  }
  .brand-tagline {
    font-family: "Open Sans", sans-serif;
    font-size: 12.5px;
    margin-top: 7px;
  }
  .save-the-date {
    position: absolute;
    left: 0;
    width: 100%;
    top: 585px;
    text-align: center;
    font-family: "Bebas Neue", sans-serif;
    font-size: 56px;
    line-height: 1;
    color: var(--white);
    letter-spacing: 0.5px;
  }
  .event-title {
    position: absolute;
    left: 0;
    width: 100%;
    top: 700px;
    text-align: center;
    font-family: "Bebas Neue", sans-serif;
    font-size: 76px;
    line-height: 1;
    color: var(--title-blue);
    letter-spacing: 1px;
  }
  .event-subtitle {
    position: absolute;
    left: 0;
    width: 100%;
    top: 766px;
    text-align: center;
    font-family: "Montserrat", sans-serif;
    font-weight: 500;
    font-size: 27px;
    color: var(--text-gray);
    letter-spacing: 1.5px;
  }
  .info-box {
    position: absolute;
    top: 846px;
    height: 90px;
    box-sizing: border-box;
    border: 1.2px solid var(--box-border);
    border-radius: 6px;
    display: flex;
    align-items: center;
    justify-content: center;
    text-align: center;
    font-family: "Oswald", sans-serif;
    color: var(--text-gray);
  }
  .info-box.date {
    left: 58px;
    width: 255px;
    font-size: 37px;
    font-weight: 500;
    padding-top: 28px;
  }
  .info-box.date .year { color: var(--title-blue); }
  .info-box.venue {
    left: 353px;
    width: 277px;
    font-size: 21px;
    line-height: 1.25;
    padding-top: 24px;
  }
  .info-icon {
    position: absolute;
    top: 812px;
    width: 60px;
    height: 60px;
  }
  .info-icon.date-icon { left: 155px; }
  .info-icon.venue-icon { left: 461px; }
  .footer-bar {
    position: absolute;
    left: 0;
    bottom: 0;
    width: 100%;
    height: 15px;
    background: var(--band-gray);
  }
</style>
</head>
<body>
  <div class="flyer">
    <svg class="flyer-art" width="682" height="962" viewBox="0 0 682 962">
      <defs>
        <linearGradient id="header-blue" x1="0" y1="0" x2="1" y2="1">
          <stop offset="0" stop-color="#1f3c8e"/>
          <stop offset="0.5" stop-color="#2f54a8"/>
          <stop offset="1" stop-color="#2a4c9f"/>
        </linearGradient>
        <linearGradient id="skyline-tones" x1="0" y1="0" x2="0" y2="1">
          <stop offset="0" stop-color="#5d9fd3"/>
          <stop offset="0.22" stop-color="#b9cfdc"/>
          <stop offset="0.35" stop-color="#eab08a"/>
          <stop offset="0.45" stop-color="#8a8c92"/>
          <stop offset="1" stop-color="#3f3d40"/>
        </linearGradient>
      </defs>
      <rect class="header-field" x="0" y="0" width="682" height="640" fill="url(#header-blue)"/>
      <circle class="skyline-photo" cx="341" cy="437" r="257" fill="url(#skyline-tones)" role="img" aria-label="Aerial photograph of a city skyline at sunset"/>
      <path class="gray-arc" d="M0 637 Q341 437 682 637 Z" fill="var(--band-gray)"/>
      <path class="green-arc" d="M0 640 Q341 462 682 640 L682 962 L0 962 Z" fill="var(--accent-green)"/>
      <path class="white-base" d="M0 640 L149 598 C200 660 270 685 341 685 C412 685 482 660 537 598 L682 640 L682 962 L0 962 Z" fill="var(--white)"/>
    </svg>

    <header class="brand">
      <div class="brand-mark"></div>
      <div class="brand-text">
        <div class="brand-name">Q-TarVM</div>
        <div class="brand-tagline">Council for Tomorrow's Venue Makers</div>
      </div>
    </header>

    <div class="save-the-date">SAVE THE DATE</div>
    <h1 class="event-title" style="margin:0">4TH ANNUAL LIFT HER</h1>
    <div class="event-subtitle">Forward &amp; See Her Rise!</div>

    <div class="info-box date"><span>January 25, <span class="year">2019</span></span></div>
    <div class="info-box venue"><span>Harbor Crest Resort &amp; Spa,<br>San Marcos, TX</span></div>

    <svg class="info-icon date-icon" viewBox="0 0 60 60" aria-hidden="true">
      <circle cx="30" cy="30" r="29" fill="var(--accent-green)"/>
      <circle cx="29" cy="31" r="26" fill="#dcdcdc"/>
      <circle cx="29" cy="30" r="24" fill="var(--brand-blue-deep)"/>
      <rect x="17" y="20" width="24" height="20" rx="2" fill="none" stroke="#fff" stroke-width="2"/>
      <line x1="17" y1="25" x2="41" y2="25" stroke="#fff" stroke-width="2"/>
      <line x1="22" y1="17" x2="22" y2="22" stroke="#fff" stroke-width="2"/>
      <line x1="36" y1="17" x2="36" y2="22" stroke="#fff" stroke-width="2"/>
      <g fill="#fff">
        <rect x="20" y="28" width="3" height="3"/><rect x="25" y="28" width="3" height="3"/><rect x="30" y="28" width="3" height="3"/><rect x="35" y="28" width="3" height="3"/>
        <rect x="20" y="33" width="3" height="3"/><rect x="25" y="33" width="3" height="3"/><rect x="30" y="33" width="3" height="3"/><rect x="35" y="33" width="3" height="3"/>
      </g>
    </svg>

    <svg class="info-icon venue-icon" viewBox="0 0 60 60" aria-hidden="true">
      <circle cx="30" cy="30" r="29" fill="var(--accent-green)"/>
      <circle cx="29" cy="31" r="26" fill="#dcdcdc"/>
      <circle cx="29" cy="30" r="24" fill="var(--brand-blue-deep)"/>
      <path d="M29 42 C22 33 20 29 20 25 A9 9 0 0 1 38 25 C38 29 36 33 29 42 Z" fill="none" stroke="#fff" stroke-width="2"/>
      <circle cx="29" cy="25" r="3.5" fill="none" stroke="#fff" stroke-width="2"/>
      <ellipse cx="29" cy="42" rx="9" ry="2.5" fill="none" stroke="#fff" stroke-width="1.5"/>
    </svg>

    <div class="footer-bar"></div>
  </div>
</body>
</html>
```